Larkfield Homecare - Website

MUST HAVE EXPERIENCE DESIGNING WEBSITES HEALTH CARE IN GENERAL AND/OR HOME NURSING SERVICES.

Details attached.

Number of Pages Required

1 page

Requirements
Must have
• Warm feel
caregivers

Color similar to the logo...

```html
<!DOCTYPE html>
<html lang="en">
<head>
<meta charset="utf-8">
<title>Larkfield Homecare</title>
<link href="https://fonts.googleapis.com/css2?family=Poppins:wght@300;400;500;600;700&display=swap" rel="stylesheet">
<style>
:root{
  --teal:#17809f;
  --teal-soft:#5fb3ad;
  --orange:#f5891f;
  --text:#7a7a7a;
  --dark:#3c3c3c;
  --grey-bg:#f5f5f5;
  --sky:#c6e9f7;
  --line:#e3e3e3;
  --white:#ffffff;
}
*{box-sizing:border-box;margin:0;padding:0}
html,body{width:1200px;height:3529px;overflow:hidden}
body{position:relative;font-family:'Poppins',sans-serif;color:var(--text);background:var(--white)}
.abs{position:absolute}
a{color:inherit;text-decoration:none}

/* header */
.hero{left:0;top:0;width:1200px;height:600px;background:linear-gradient(100deg,#6fb9ad 0%,#8ebf9a 35%,#c9b37a 65%,#e9a257 100%)}
.hero-wave{left:0;top:360px;width:1200px;height:240px}
.brand{left:133px;top:0;width:172px;height:85px;background:var(--white);border-radius:0 0 6px 6px;box-shadow:0 3px 12px rgba(0,0,0,.08);display:flex;align-items:center;justify-content:center;gap:8px}
.brand-dot{width:22px;height:22px;border-radius:50%;background:var(--orange)}
.brand-name{font-size:14px;font-weight:600;color:var(--teal);line-height:1.1}
.nav{left:420px;top:40px;display:flex;gap:19px;font-size:11px;color:#3e4f55}
.nav .active{border-bottom:1px solid #3e4f55}
.nav-call{left:817px;top:40px;font-size:10px;color:#3e4f55}
.btn{display:flex;align-items:center;justify-content:center;border-radius:20px;font-size:10px;font-weight:500}
.btn-orange{background:var(--orange);color:var(--white)}
.btn-ghost{border:1.5px solid var(--white);color:var(--white)}
.join{left:955px;top:36px;width:110px;height:24px}
.hero-title{left:200px;top:182px;width:460px;font-size:26px;font-weight:400;color:var(--white);line-height:1.22}
.hero-contact{left:200px;top:309px;width:100px;height:30px}
.hero-more{left:312px;top:309px;width:75px;height:30px}

/* about */
.about-head{left:312px;top:633px;font-size:13px;color:var(--dark)}
.about-head b{font-weight:500;color:var(--teal)}
.about-head b span{color:var(--orange)}
.about-text{left:312px;top:668px;width:576px;font-size:10.6px;line-height:16.5px;text-align:justify}
.about-text p+p{margin-top:16px}
.link-more{font-size:9.5px;color:var(--orange)}

/* services */
.services{left:0;top:867px;width:1200px;height:868px;background:var(--grey-bg)}
.section-title{width:1200px;left:0;text-align:center;font-size:23px;font-weight:600;color:var(--teal);letter-spacing:.5px}
.section-title span{font-weight:400;margin:0 12px}
.sub-head{font-size:16px;font-weight:500;color:var(--orange)}
.body-text{font-size:10.8px;line-height:19px}
.sub-teal{font-size:12px;font-weight:500;color:var(--teal);line-height:17px}
.ticks{list-style:none;font-size:10.8px;line-height:19px}
.ticks li::before{content:"➝";color:var(--teal);font-size:9px;margin-right:8px}
.photo{border-radius:10px}
.nurse-photo{left:612px;top:996px;width:294px;height:253px;background:linear-gradient(135deg,#d9e6ea,#eef3f4 45%,#7cc6c3)}
.care-list{left:932px;top:995px;font-size:10.5px;line-height:21.3px}
.care-list h4{font-size:11.5px;font-weight:500;color:var(--orange);margin-bottom:4px}
.care-list .more{color:var(--orange);text-decoration:underline}
.divider{left:133px;top:1312px;width:931px;height:1px;background:var(--line)}
.baby-photo{left:134px;top:1375px;width:356px;height:296px;background:linear-gradient(120deg,#f4efe9,#e9c9a5 55%,#c88b63)}
.feature{top:1511px;width:116px;height:100px;background:var(--white);border:1px solid #ececec;border-radius:3px;text-align:center;padding-top:16px}
.feature svg{display:block;margin:0 auto 6px}
.feature span{font-size:10px;color:var(--text);line-height:12px;display:block}

/* testimonials */
.quote-circle{left:570px;top:1851px;width:60px;height:60px;border-radius:50%;background:#f0f0f0;display:flex;align-items:center;justify-content:center;font-size:40px;font-weight:700;color:var(--orange);line-height:1;padding-top:14px}
.testi-text{left:255px;top:1929px;width:690px;text-align:center;font-size:10.8px;line-height:17.5px}
.testi-meta{left:0;top:2001px;width:1200px;display:flex;justify-content:center;align-items:center;gap:14px;font-size:9px}
.testi-meta .name{font-size:10.5px;font-weight:500;color:var(--teal)}
.testi-meta .sep{width:1px;height:12px;background:#ccc}
.dots{left:0;top:2038px;width:1200px;display:flex;justify-content:center;align-items:center;gap:8px;font-size:9px;color:var(--orange)}
.dot{width:8px;height:8px;border-radius:50%;border:1px solid #aaa}
.dot.on{background:var(--teal);border-color:var(--teal);width:9px;height:9px}

/* covid */
.covid{left:0;top:2117px;width:1200px;height:305px;background:var(--sky)}
.covid-art{left:226px;top:2169px;width:301px;height:215px;border-radius:50%;background:radial-gradient(circle,#e9f6fb 0%,#bfe3f2 55%,rgba(198,233,247,0) 72%)}
.covid-title{left:603px;top:2197px;font-size:22px;font-weight:600;color:var(--teal)}
.covid-title span{font-weight:400;margin-left:8px}
.covid-sub{left:603px;top:2240px;font-size:16px;font-weight:600;color:#1e2a30}
.covid-text{left:603px;top:2268px;width:400px;font-size:10.8px;line-height:18px;color:#3c4a50}

/* news */
.news-card{left:195px;top:2556px;width:376px;height:313px;border-radius:6px;overflow:hidden;box-shadow:0 4px 18px rgba(0,0,0,.08);background:linear-gradient(110deg,#ece6dd,#d9b99a 50%,#f3ede6)}
.news-box{left:0;bottom:0;width:277px;height:118px;background:var(--white);padding:36px 0 0 31px}
.news-box small{font-size:8px}
.news-box p{font-size:10.5px;line-height:16px;color:#3c3c3c;margin-top:9px}
.press{left:630px;top:2570px;width:377px}
.press h5{font-size:8.5px;font-weight:600;letter-spacing:1.3px;color:var(--orange);padding-bottom:11px;border-bottom:1px solid var(--line)}
.press-item{border-bottom:1px solid var(--line);padding:16px 0 12px}
.press-item p{font-size:10.3px;line-height:15px;color:#3c3c3c}
.press-item small{display:block;margin-top:6px;font-size:8px;font-weight:500;color:#555;letter-spacing:.5px}

/* footer */
.footer-bg{left:0;top:2920px;width:1200px;height:609px}
.quote-title{left:0;top:3114px;width:1200px;text-align:center;font-size:26px;font-weight:500;color:var(--white)}
.quote-title span{font-weight:300}
.quote-sub{left:0;top:3153px;width:1200px;text-align:center;font-size:8.5px;color:var(--white)}
.field{height:30px;background:var(--white);border-radius:16px;font-size:9px;color:#aaa;padding:9px 18px}
.field.msg{height:73px;border-radius:14px}
.quote-btn{left:532px;top:3395px;width:136px;height:29px}
.social{left:1026px;width:24px;height:24px;border-radius:50%;background:rgba(255,255,255,.9)}
.copy{left:134px;top:3471px;font-size:9px;color:#3b4a40}
.call{left:0;top:3460px;width:1200px;text-align:center;font-size:18px;color:#26343a}
.call b{font-weight:600}
.mail{left:0;top:3486px;width:1200px;text-align:center;font-size:8.5px;color:#26343a}
.foot-links{left:838px;top:3471px;font-size:9px;color:#26343a;display:flex;gap:8px}
</style>
</head>
<body>

<!-- HERO -->
<div class="abs hero" role="img" aria-label="Photo of a caregiver smiling with an elderly woman at home"></div>
<svg class="abs hero-wave" viewBox="0 0 1200 240" preserveAspectRatio="none" aria-hidden="true">
  <path d="M0 17 C140 40 250 210 470 202 C690 195 760 20 930 18 C1060 16 1120 90 1200 140 L1200 240 L0 240 Z" fill="#fff"/>
</svg>

<div class="abs brand"><span class="brand-dot"></span><span class="brand-name">LARKFIELD<br>HOMECARE</span></div>
<nav class="abs nav">
  <a class="active">Home</a><a>About Us</a><a>Services</a><a>Testimonials</a><a>News</a><a>Contact Us</a>
</nav>
<div class="abs nav-call">Call &nbsp;✆ + 1 800 555 01 42</div>
<a class="abs btn btn-orange join">Join our Team</a>

<h1 class="abs hero-title">Lorem ipsum dolor sit amet, consectetur adipiscing elit, sed do eiusmod tempor.</h1>
<a class="abs btn btn-orange hero-contact">Contact Us</a>
<a class="abs btn btn-ghost hero-more">More</a>

<!-- ABOUT -->
<h2 class="abs about-head"><b>Larkfield <span>Homecare</span></b> Specialize</h2>
<div class="abs about-text">
  <p>Everyone should be free to experience joy and optimism in their lives, regardless of their age or condition. Larkfield Homecare provides a range of services that are tailored to meet the patient's needs, helping them to maintain their independence and live happy and fulfilling lives.</p>
  <p>Larkfield Homecare deliver comprehensive care to new porn baby and mother, and elderly in the comfort of their own homes, we ensure that the needs of our clients and their families are at the heart of everything they do.</p>
  <p><a class="link-more">Our Company →</a></p>
</div>

<!-- SERVICES -->
<section class="abs services"></section>
<h2 class="abs section-title" style="top:922px"><span>--</span>SERVICES<span>--</span></h2>

<h3 class="abs sub-head" style="left:133px;top:992px">Home Nursing Services</h3>
<p class="abs body-text" style="left:133px;top:1031px;width:445px">Looking for care, custodial care, Urinary catheterization care, Wound care, Injections, IV infusions, Vaccination or other nursing assistance? Get all of this, and more in the comfort of your home by highly qualified and experienced nurses.</p>
<p class="abs sub-teal" style="left:133px;top:1113px">Deliver the best choices for people who require<br>24-hour medical care and supervision.</p>
<ul class="abs ticks" style="left:133px;top:1155px">
  <li>Monitoring of medication</li>
  <li>Personal care &nbsp;(including dressing, bathing, and toilet assistance)</li>
  <li>Weekend and holiday care</li>
  <li>Social and recreational activities</li>
</ul>
<div class="abs photo nurse-photo" role="img" aria-label="Photo of a smiling nurse holding a clipboard in a clinic"></div>
<div class="abs care-list">
  <h4>Care Offered</h4>
  Cancer Care<br>Companionship<br>Dementia<br>Elderly Care<br>Hospital Discharge<br>Learning Disability<br>Medication Assistance<br>Mental Health Condition<br>Palliative Care<br><a class="more">more</a>
</div>

<div class="abs divider"></div>

<div class="abs photo baby-photo" role="img" aria-label="Photo of a mother holding her newborn baby"></div>
<h3 class="abs sub-head" style="left:549px;top:1371px">New Born Baby And Mother Care At Home</h3>
<p class="abs body-text" style="left:549px;top:1410px;width:515px">Worried about your newborn's needs? Facing issues in coping up with the initial challenges of feeding infant child and post-operative recovery? (New Born Baby &amp; Mother Care), a post-natal care program from Larkfield Homecare and enjoy the joys of motherhood without the worries.</p>

<div class="abs feature" style="left:549px">
  <svg width="34" height="34" viewBox="0 0 34 34" fill="none" stroke="#17809f" stroke-width="1.6"><circle cx="17" cy="17" r="13"/><circle cx="17" cy="17" r="6"/></svg>
  <span>New born baby<br>care</span>
</div>
<div class="abs feature" style="left:674px">
  <svg width="34" height="34" viewBox="0 0 34 34" fill="none" stroke="#17809f" stroke-width="1.6"><circle cx="17" cy="11" r="6"/><path d="M7 31c0-7 4-11 10-11s10 4 10 11"/></svg>
  <span>Breastfeeding<br>care</span>
</div>
<div class="abs feature" style="left:798px">
  <svg width="34" height="34" viewBox="0 0 34 34" fill="none" stroke="#17809f" stroke-width="1.6"><circle cx="17" cy="17" r="13" stroke-dasharray="4 2"/><circle cx="17" cy="17" r="7"/></svg>
  <span>Personalized<br>care</span>
</div>
<div class="abs feature" style="left:922px">
  <svg width="34" height="34" viewBox="0 0 34 34" fill="none" stroke="#17809f" stroke-width="1.6"><path d="M17 29 5 17a7 7 0 0 1 12-9 7 7 0 0 1 12 9Z"/><path d="M8 17h6l2-4 3 7 2-3h5"/></svg>
  <span>Post-delivery<br>mother care</span>
</div>
<p class="abs body-text" style="left:549px;top:1632px">Our core care services include providing private duty nursing and home health..</p>
<a class="abs link-more" style="left:549px;top:1655px">Read more →</a>

<!-- TESTIMONIALS -->
<h2 class="abs section-title" style="top:1791px"><span>--</span>TESTIMONIALS<span>--</span></h2>
<div class="abs quote-circle">“</div>
<p class="abs testi-text">Lorem Ipsum is simply dummy text of the printing and typesetting industry. Lorem Ipsum has been the industry's standard dummy text ever since the 1500s, when an unknown printer took a galley of type and scrambled it to make a type specimen book. It has survived not only five centuries, but also the leap...</p>
<div class="abs testi-meta">
  <span>
    <svg width="11" height="11" viewBox="0 0 12 12" fill="none" stroke="#17809f" stroke-width="1.2" style="vertical-align:-2px;margin-right:5px"><rect x="1" y="2" width="10" height="9" rx="1"/><path d="M1 5h10M4 1v2M8 1v2"/></svg>30 Nov, 2020
  </span>
  <span class="sep"></span>
  <span class="name">Marta Ellison</span>
</div>
<div class="abs dots"><span class="dot"></span><span class="dot on"></span><span class="dot"></span><span style="margin-left:8px">View All →</span></div>

<!-- COVID -->
<section class="abs covid"></section>
<div class="abs covid-art" role="img" aria-label="Illustration of a masked family behind a shield surrounded by virus particles"></div>
<h2 class="abs covid-title">CORONAVIRUS UPDATE<span>--</span></h2>
<h3 class="abs covid-sub">Protect Your Family From Covid</h3>
<p class="abs covid-text">Lorem Ipsum is simply dummy text of the printing and typesetting industry. Lorem Ipsum has been the industry's</p>
<a class="abs link-more" style="left:603px;top:2325px">Read more →</a>

<!-- NEWS -->
<h2 class="abs section-title" style="top:2484px"><span>--</span>NEWS<span>--</span></h2>
<article class="abs news-card" role="img" aria-label="Photo of an adult daughter embracing her smiling elderly mother">
  <div class="abs news-box">
    <small>Apr 2 2021 &nbsp;|&nbsp; By Admin</small>
    <p>7 Ways to Bring Hope and Spread<br>Kindness this National Month of Hope</p>
  </div>
</article>
<div class="abs press">
  <h5>PRESS RELEASE</h5>
  <div class="press-item"><p>Lorem ipsum dolor sit amet, consectetur adipiscing elit, sed do eiusmod tempor incididunt ut labore et dolore magna aliqua</p><small>JUN 26 2021</small></div>
  <div class="press-item"><p>Lorem ipsum dolor sit amet, consectetur adipiscing elit, sed do eiusmod tempor incididunt ut labore et dolore magna aliqua</p><small>JUN 26 2021</small></div>
  <div class="press-item"><p>Lorem ipsum dolor sit amet, consectetur adipiscing elit, sed do eiusmod tempor incididunt ut labore et dolore magna aliqua</p><small>JUN 26 2021</small></div>
  <a class="link-more" style="display:block;margin-top:16px">Explore All →</a>
</div>

<!-- FOOTER / QUOTE -->
<svg class="abs footer-bg" viewBox="0 0 1200 609" preserveAspectRatio="none" aria-hidden="true">
  <defs>
    <linearGradient id="footGrad" x1="0" y1="1" x2="1" y2="0">
      <stop offset="0" stop-color="#5fb3ad"/>
      <stop offset=".45" stop-color="#a4a35e"/>
      <stop offset="1" stop-color="#ee9a3c"/>
    </linearGradient>
  </defs>
  <path d="M0 46 C180 90 330 150 560 128 C790 105 930 10 1200 12 L1200 609 L0 609 Z" fill="url(#footGrad)"/>
  <path d="M1200 160 C1020 180 900 290 930 400 C960 500 1080 520 1200 500 Z" fill="#b59846" opacity=".35"/>
</svg>

<h2 class="abs quote-title"><span>-- </span>Get A Quick Quote<span> --</span></h2>
<p class="abs quote-sub">Duis aute irure dolor in reprehenderit in voluptate velit esse cillum dolore eu fugiat nulla.</p>
<div class="abs field" style="left:312px;top:3195px;width:277px">Enter your Name</div>
<div class="abs field" style="left:610px;top:3195px;width:278px">Email</div>
<div class="abs field" style="left:312px;top:3245px;width:277px">Phone</div>
<div class="abs field" style="left:610px;top:3245px;width:278px">Subject</div>
<div class="abs field msg" style="left:312px;top:3295px;width:576px">Message ...</div>
<a class="abs btn btn-orange quote-btn">Request A Quote</a>

<span class="abs social" style="top:3127px"></span>
<span class="abs social" style="top:3168px"></span>
<span class="abs social" style="top:3209px"></span>
<span class="abs social" style="top:3250px"></span>

<div class="abs copy">© 2021 by Larkfield Homecare</div>
<div class="abs call">Call, <b>+ 1 800 555 0142</b></div>
<div class="abs mail">E info@larkfield-homecare.com</div>
<nav class="abs foot-links"><a>Home</a>|<a>Company</a>|<a>Contact</a>|<a>Join our Team</a></nav>

</body>
</html>
```